New boutique hotel for tourists, with hint of art deco styling

This is a new, soon to be completed, boutique hotel in Sydney. A letterhead with a logo is required. Less emphasis on the word "boutique". Perhaps the word could be screened to be lighter in colour (or print intensity). Would like a simple, clear, easy-to read, sans serif type face. The information on the letterhead is:
Mrs Fennel Boutique Hotel
417 Larkmoor Street,
Wellbrook, NSW, 2094
Australia
Tel: +61 2 9704-5512
mrsfennelhotel@example-mail.com
mrsfennelhotel.example.au
ABN 47 902 365 148

Target Market(s)

travellers, tourists, various ages

Industry/Entity Type

Hospitality

Contact Information for Business Card

Mrs Fennel Boutique Hotel
417 Larkmoor Street,
Wellbrook, NSW, 2097
Telephone: (02) 9704-5512
www.mrsfennelhotel.example.au
mrsfennelhotel@example-mail.com
ABN 47 902 365 148

Logo Text

suggest playing with the letter "B"

Font styles to use
Sans Serif

Colors
3176b5

Requirements
Must have
• ABN to be very small.
• Must be clear, easy to read and in a sans serif typeface, please!
Nice to have
• The word "Boutique" should be less intense in appearance to the rest of the name, or even "Boutique Hotel" can have less prominence than "Mrs Fennel".
Should not have
• No serif typeface. Sans serif only will be accepted.

```html
<!DOCTYPE html>
<html lang="en">
<head>
<meta charset="utf-8">
<title>Mrs Fennel Boutique Hotel – Stationery</title>
<link href="https://fonts.googleapis.com/css2?family=Source+Sans+3:wght@400;600&display=swap" rel="stylesheet">
<style>
  :root{
    --brand:#3176b5;
    --ink:#2b2b2b;
    --muted:#6f6f6f;
    --rule:#9a9a9a;
    --paper:#ffffff;
    --card:#f1f1f1;
    --backdrop:#e4e1dc;
    --sign:#8fb2d8;
  }
  *{box-sizing:border-box;margin:0;padding:0}
  html,body{width:1200px;height:900px;overflow:hidden}
  body{background:var(--backdrop);position:relative;font-family:"Source Sans 3",sans-serif;color:var(--ink)}

  /* Name lockup: one line, one colour, one weight */
  .brand{display:flex;align-items:center;gap:10px}
  .brand-mark{background:var(--brand);flex:none}
  .brand-name{font-family:"Source Sans 3",sans-serif;font-weight:400;color:var(--ink);line-height:1;white-space:nowrap}

  /* Letterhead */
  .letterhead{position:absolute;left:458px;top:22px;width:535px;height:693px;background:var(--paper);box-shadow:0 2px 8px rgba(0,0,0,.12)}
  .letterhead__brand{position:absolute;left:70px;top:48px}
  .letterhead__brand .brand-mark{width:30px;height:30px}
  .letterhead__brand .brand-name{font-size:22px}

  .letter{position:absolute;left:70px;top:158px;width:400px;font-size:9.6px;line-height:15px}
  .letter__salutation{font-size:12px;margin-bottom:34px}
  .letter p{text-align:justify;margin-bottom:15px}
  .letter__closing{position:absolute;left:70px;top:518px;width:400px;text-align:right;font-size:10px}
  .signature{display:block;margin:8px 0 0 auto;width:48px;height:14px;background:var(--sign);opacity:.45;border-radius:7px}

  .letterhead__footer{position:absolute;left:70px;top:638px;width:400px;border-top:1px solid var(--rule);padding-top:6px;display:flex;gap:30px;font-size:6px;color:var(--muted);line-height:8px}
  .footer__box{width:22px;height:22px;border:1px solid var(--rule);flex:none}
  .footer__col{display:flex;flex-direction:column;gap:4px}
  .footer__item{display:flex;gap:5px}
  .dot{width:6px;height:6px;border:1px solid var(--rule);border-radius:50%;flex:none;margin-top:1px}
  .footer__abn{position:absolute;left:70px;top:674px;font-size:5.5px;color:var(--muted)}

  /* Business cards */
  .card{position:absolute;top:708px;width:256px;height:150px;background:var(--card);box-shadow:0 2px 6px rgba(0,0,0,.12)}
  .card--back{left:76px}
  .card--front{left:356px;display:flex;align-items:center;justify-content:center}
  .card__brand{position:absolute;left:16px;top:22px;gap:7px}
  .card__brand .brand-mark{width:22px;height:22px}
  .card__brand .brand-name{font-size:14px}
  .card__address{position:absolute;left:16px;top:104px;font-size:6.5px;line-height:7.5px}
  .card__contacts{position:absolute;right:14px;top:96px;font-size:6.5px;line-height:7.5px;display:flex;flex-direction:column;gap:3px;align-items:flex-end}
  .card__contacts .footer__item{align-items:center}
  .card__contacts .dot{border-color:var(--brand);background:#cfe0f0;margin:0}
  .card__abn{position:absolute;left:16px;top:138px;font-size:4.5px;color:var(--muted)}
  .card--front .brand-name{font-size:17px}
</style>
</head>
<body>

<article class="letterhead">
  <header class="brand letterhead__brand">
    <span class="brand-mark"></span>
    <span class="brand-name">Mrs Fennel Boutique Hotel</span>
  </header>

  <section class="letter">
    <p class="letter__salutation">Dear Mr. Hartley,</p>
    <p>Lorem ipsum dolor sit amet, consectetur adipiscing elit. Donec orci purus, luctus vitae dignissim eu, iaculis sed purus. Vivamus faucibus, ipsum nec aliquet viverra, leo mauris condimentum ligula, sit amet sagittis enim ligula quis arcu. Nam egestas tortor id nisi porttitor mattis. In tortor ante, ultricies in suscipit a, tempus non massa. Vivamus et auctor mi. Fusce vel massa nulla. Phasellus nec eros mauris, et scelerisque orci.</p>
    <p>Donec malesuada orci vitae nulla accumsan porta a id massa. Quisque accumsan iaculis magna sit amet fringilla. Maecenas consequat, magna eget tincidunt semper, odio nibh rutrum mi, id feugiat ante nisi eu risus. Vestibulum nunc orci, rhoncus a placerat in, ultricies in mi. Cras mattis varius eros, vel fringilla nisi suscipit eget. Quisque scelerisque sagittis nulla at porttitor.</p>
    <p>Sed id augue vitae urna euismod commodo aliquet a quam. Pellentesque arcu velit, cursus et malesuada ut, consequat et diam. Nullam erat sem, rhoncus id ullamcorper vitae, rhoncus et arcu. In ultricies ultricies nulla, ut rutrum nisi iaculis at. Donec eu magna a metus ornare faucibus. Fusce aliquet faucibus ultricies. Morbi semper, est id tincidunt gravida, sem arcu adipiscing lacus, ac bibendum nulla leo eu purus. Quisque nec diam sed risus consectetur a ccumsan quis quis nibh. Vestibulum id purus lorem.</p>
  </section>

  <div class="letter__closing">
    Sincerely,
    <span class="signature" role="img" aria-label="Handwritten signature"></span>
  </div>

  <footer class="letterhead__footer">
    <span class="footer__box"></span>
    <div class="footer__col">
      <div class="footer__item"><span class="dot"></span><span>417 Larkmoor Street,<br>Wellbrook, NSW, 2094<br>Australia</span></div>
    </div>
    <div class="footer__col">
      <div class="footer__item"><span class="dot"></span><span>+61 2 9704-5512</span></div>
      <div class="footer__item"><span class="dot"></span><span>mrsfennelhotel@example-mail.com</span></div>
    </div>
    <div class="footer__col">
      <div class="footer__item"><span class="dot"></span><span>mrsfennelhotel.example.au</span></div>
    </div>
  </footer>
  <p class="footer__abn">ABN 47 902 365 148</p>
</article>

<article class="card card--back">
  <div class="brand card__brand">
    <span class="brand-mark"></span>
    <span class="brand-name">Mrs Fennel Boutique Hotel</span>
  </div>
  <p class="card__address">417 Larkmoor Street,<br>Wellbrook, NSW, 2097<br>Australia</p>
  <div class="card__contacts">
    <div class="footer__item"><span>(02) 9704-5512</span><span class="dot"></span></div>
    <div class="footer__item"><span>mrsfennelhotel@example-mail.com</span><span class="dot"></span></div>
    <div class="footer__item"><span>www.mrsfennelhotel.example.au</span><span class="dot"></span></div>
  </div>
  <p class="card__abn">ABN 47 902 365 148</p>
</article>

<article class="card card--front">
  <span class="brand-name">Mrs Fennel Boutique Hotel</span>
</article>

</body>
</html>
```